Logo/ business card idea for a weld inspection/ nondestructive testing LLC

I have just started an LLC (my first) for weld inspection and non-destructive testing. I am the president and only member of this company. It is a very niche industry and word of mouth is basically the only advertisement needed to get you the next job. I will offer magnetic particle, dye penetrant, ultrasonic, and visual testing for the non-destructive services. X-ray is a form of non-destructive testing that I spent a few years doing but to costly for me at this time. All pipelines under the ground are welded, visually inspected and x-ray by someone just like me. All new building construction, any type of nuclear plant , pressure vessel, ect. , the welds are inspected by someone like me. Its is every increasing also with safety concerns. People are living right next to this stuff!!I will be the guy that fabrication shops or construction companies call to give the final OK that the welds are satisfactory after inspection to a certain code or standard. The designers have all the freedom they wish but I have attached a PDF with greater explanations and color ideas. I want raised glossy print on the front of the card and the necessary info. The back will not have raised print and serve more as a brief resume listing the certifications I have. The company only cares about the certifications and ultimately my signature. I want to make the front of the car into a fridge magnet to pass out with the card also. Something that is appealing to hang up instead of getting lost in someones wallet. The final design………. should be classic and stand the test of time. It should communicate precision and accuracy as well as incorporate the sound beam you will find in the PDF I’ve attached.Thanks and have a great day,Dwayne

Target Market(s)

Adult males in english speaking countries that handle welding and/or construction duties. Most of the time under heavy time constraints and deadlines. Ages 30-60

Industry/Entity Type

Construction

Contact Information for Business Card

Halvern Inspection Services, LLC
Dwayne Halvern
Ithaca, MI
989-517-2438
halv7dw@mailtrove.net

Font styles to use
Other font styles liked:
• designers choice

Requirements
Nice to have
• The logo on the front can completely encase the Halvern, be segmented incorporating the Halvern, or next to it. There can also be a couple of “flaws” (the red, blue and yellow in some of the pictures attached in the PDF) in the sound beam spread.

```html
<!DOCTYPE html>
<html lang="en">
<head>
<meta charset="utf-8">
<title>Halvern Inspection Services, LLC — Business Card</title>
<link rel="stylesheet" href="https://fonts.googleapis.com/css2?family=Saira:wght@400;500&family=Saira+Condensed:wght@300;400&family=Saira+Semi+Condensed:wght@400&display=swap">
<style>
  :root {
    --bg-light: #dcf1fb;
    --bg-mid: #6ccdf6;
    --bg-deep: #2584ee;
    --bg-darkest: #0b4ccd;
    --card-left: #a6d2f8;
    --card-right: #c9e6fc;
    --card-back-left: #b3daf9;
    --card-back-right: #d2ecfc;
    --brand-blue: #2b31c9;
    --ink-navy: #1b1f86;
    --ink-list: #1d2272;
    --corner-tone: rgba(255, 255, 255, 0.35);
  }
  * { box-sizing: border-box; margin: 0; padding: 0; }
  html, body { width: 1200px; height: 565px; overflow: hidden; }
  body {
    position: relative;
    background: linear-gradient(90deg, var(--bg-light) 0%, var(--bg-mid) 45%, var(--bg-deep) 80%, var(--bg-darkest) 100%);
    font-family: "Saira", sans-serif;
  }
  .card {
    position: absolute;
    width: 493px;
    height: 274px;
    overflow: hidden;
  }
  .card--front {
    left: 84px; top: 139px;
    background: linear-gradient(90deg, var(--card-left), var(--card-right));
  }
  .card--back {
    left: 618px; top: 137px;
    background: linear-gradient(90deg, var(--card-back-left), var(--card-back-right));
  }
  .corner-accent {
    position: absolute;
    right: 0; bottom: 0;
    width: 110px; height: 110px;
    background: linear-gradient(135deg, transparent 50%, var(--corner-tone) 50%);
  }
  .brand { position: absolute; color: var(--brand-blue); font-family: "Saira", sans-serif; font-weight: 400; }
  .brand__mark {
    position: absolute;
    width: 58px; height: 58px;
    border-radius: 50%;
    background: var(--brand-blue);
  }
  .brand__name { position: absolute; white-space: nowrap; line-height: 1; }
  .brand__name--main { font-size: 54px; letter-spacing: 1px; }
  .brand__name--sub { font-size: 16px; letter-spacing: 0.5px; }

  .card--front .brand__mark { left: 150px; top: 48px; }
  .card--front .brand__name--main { left: 222px; top: 66px; }
  .card--front .brand__name--sub { left: 234px; top: 126px; }

  .card--back .brand__mark { left: 92px; top: 42px; }
  .card--back .brand__name--main { left: 162px; top: 60px; }
  .card--back .brand__name--sub { left: 176px; top: 120px; }

  .contact { position: absolute; left: 16px; top: 180px; color: var(--ink-navy); }
  .contact__name {
    font-family: "Saira Condensed", sans-serif;
    font-weight: 300;
    font-size: 42px;
    line-height: 1;
    white-space: nowrap;
  }
  .contact__phone {
    font-family: "Saira Condensed", sans-serif;
    font-weight: 400;
    font-size: 21px;
    line-height: 1;
    margin-top: 6px;
  }
  .contact__email {
    font-family: "Saira Condensed", sans-serif;
    font-weight: 400;
    font-size: 15.5px;
    line-height: 1;
    margin-top: 4px;
  }

  .credentials {
    position: absolute;
    left: 16px; top: 162px;
    list-style: none;
    color: var(--ink-list);
    font-family: "Saira Semi Condensed", sans-serif;
    font-size: 14.5px;
    line-height: 18px;
  }
  .credentials__sub {
    list-style: none;
    padding-left: 68px;
    font-size: 11px;
    line-height: 16px;
  }
</style>
</head>
<body>
  <section class="card card--front" aria-label="Business card front">
    <div class="brand">
      <span class="brand__mark"></span>
      <span class="brand__name brand__name--main">Halvern</span>
      <span class="brand__name brand__name--sub">Inspection Services, LLC</span>
    </div>
    <div class="contact">
      <p class="contact__name">Dwayne Halvern</p>
      <p class="contact__phone">989-517-2438</p>
      <p class="contact__email">halv7dw@mailtrove.net</p>
    </div>
    <div class="corner-accent" role="img" aria-label="Fine diagonal line texture in the corner"></div>
  </section>

  <section class="card card--back" aria-label="Business card back">
    <div class="brand">
      <span class="brand__mark"></span>
      <span class="brand__name brand__name--main">Halvern</span>
      <span class="brand__name brand__name--sub">Inspection Services, LLC</span>
    </div>
    <ul class="credentials">
      <li>NWQB Certified Welding Inspector</li>
      <li>NWQB Certified Radiographic Interpreter</li>
      <li>NWQB Certified Welding Educator</li>
      <li>Level II - Ultrasonic Testing
        <ul class="credentials__sub">
          <li>Magnetic Particle Testing</li>
          <li>Liquid Penetrant Testing</li>
        </ul>
      </li>
    </ul>
    <div class="corner-accent" role="img" aria-label="Fine diagonal line texture in the corner"></div>
  </section>
</body>
</html>
```